11x 11 - KIVO Program Flyer

Introducing The KIVO PROGRAM

The BEST DPA Product on the Planet
* Lowest Zarn in the Industry - 580 Minimum
* Nothing Down - 100% GTU Purchase Financing
* One Submission, One Approval and One Closing
* No Income Limits, No DTI Restrictions, No Property Restrictions

Call (800) 471-9026 for more information

RLCB #738160
www.2ndlanehomes.com

```html
<!DOCTYPE html>
<html lang="en">
<head>
<meta charset="utf-8">
<title>KIVO Program Flyer</title>
<link rel="stylesheet" href="https://fonts.googleapis.com/css2?family=Arimo:ital,wght@0,400;0,700;1,400&display=swap">
<style>
  :root {
    --paper: #ffffff;
    --ink-dark: #141210;
    --stage-grey: #4a4846;
    --wood: #8a6a4f;
    --text-light: #ffffff;
    --seal-fill: #c29a55;
    --brand-ink: #2a5aa6;
  }
  * { margin: 0; padding: 0; box-sizing: border-box; }
  html, body { width: 1200px; height: 1200px; overflow: hidden; background: var(--paper); }
  body { position: relative; font-family: "Arimo", Arial, sans-serif; color: var(--text-light); }

  .flyer { position: absolute; left: 205px; top: 205px; width: 797px; height: 797px; overflow: hidden; background: var(--ink-dark); }
  .flyer > * { position: absolute; }

  .stage-photo {
    inset: 0;
    background:
      radial-gradient(ellipse 240px 200px at 590px 50px, rgba(255,255,255,0.35), transparent 70%),
      linear-gradient(180deg, #1c1b1a 0%, #3a3836 30%, var(--stage-grey) 45%, #5a5047 62%, var(--wood) 72%, #3b2c20 86%, var(--ink-dark) 96%);
  }
  .couple-photo {
    left: 396px; top: 305px; width: 401px; height: 370px;
    background: radial-gradient(ellipse at 55% 55%, #b08662 0%, #6e4e38 45%, rgba(40,30,25,0) 80%);
    border-radius: 40% 40% 10% 10%;
  }

  .kicker { left: 56px; top: 64px; font-size: 42px; font-style: italic; letter-spacing: 11px; }
  .title { left: 56px; top: 122px; font-size: 76px; line-height: 72px; font-weight: 400; letter-spacing: -1px; }
  .title strong { font-weight: 700; }

  .seal { left: 485px; top: 68px; width: 218px; height: 218px; border-radius: 50%; background: var(--seal-fill); }
  .slogan { left: 56px; top: 282px; font-size: 17px; font-weight: 700; letter-spacing: 0.5px; }

  .benefits { left: 56px; top: 333px; width: 380px; list-style: none; }
  .benefits li { position: relative; padding-left: 32px; font-size: 20px; line-height: 26px; margin-bottom: 17px; text-shadow: 1px 1px 2px rgba(0,0,0,0.8); }
  .benefits svg { position: absolute; left: 0; top: 4px; width: 17px; height: 17px; }

  .brand-box { left: 56px; top: 690px; width: 120px; height: 72px; background: var(--paper); display: flex; align-items: center; justify-content: center; gap: 6px; padding: 0 8px; }
  .brand-box .mark { width: 10px; height: 10px; border-radius: 50%; background: var(--brand-ink); flex: none; }
  .brand-box span { font-size: 11px; font-weight: 700; color: var(--brand-ink); line-height: 13px; }

  .contact { left: 196px; top: 686px; }
  .contact .phone { font-size: 25px; font-weight: 700; line-height: 30px; }
  .contact .more { font-size: 17px; font-style: italic; line-height: 22px; }
  .contact .web { font-size: 14px; letter-spacing: 2.2px; margin-top: 9px; }

  .housing-badge { left: 667px; top: 665px; width: 56px; height: 56px; border: 5px solid var(--text-light); border-radius: 4px; }
  .license { left: 640px; top: 738px; width: 110px; height: 26px; border: 1px solid var(--text-light); font-size: 14px; font-weight: 700; display: flex; align-items: center; justify-content: center; }
</style>
</head>
<body>
<main class="flyer">
  <div class="stage-photo" role="img" aria-label="Empty room with spotlight and wooden floor"></div>
  <div class="couple-photo" role="img" aria-label="Happy couple, woman sitting in a moving box pushed by her partner"></div>

  <p class="kicker">INTRODUCING</p>
  <h1 class="title">The <strong>KIVO</strong><br><strong>PROGRAM</strong></h1>

  <div class="seal" aria-hidden="true"></div>
  <p class="slogan">The BEST DPA Product on the Planet</p>

  <ul class="benefits">
    <li><svg viewBox="0 0 20 20"><circle cx="10" cy="10" r="8" fill="none" stroke="#fff" stroke-width="2.5"/><path d="M5 10l4 4 9-11" fill="none" stroke="#fff" stroke-width="2.5"/></svg><strong>Lowest Zarn in the Industry</strong><br>- 580 Minimum</li>
    <li><svg viewBox="0 0 20 20"><circle cx="10" cy="10" r="8" fill="none" stroke="#fff" stroke-width="2.5"/><path d="M5 10l4 4 9-11" fill="none" stroke="#fff" stroke-width="2.5"/></svg><strong>Nothing Down</strong> - 100% GTU<br>Purchase Financing</li>
    <li><svg viewBox="0 0 20 20"><circle cx="10" cy="10" r="8" fill="none" stroke="#fff" stroke-width="2.5"/><path d="M5 10l4 4 9-11" fill="none" stroke="#fff" stroke-width="2.5"/></svg><strong>One Submission, One Approval<br>and One Closing</strong></li>
    <li><svg viewBox="0 0 20 20"><circle cx="10" cy="10" r="8" fill="none" stroke="#fff" stroke-width="2.5"/><path d="M5 10l4 4 9-11" fill="none" stroke="#fff" stroke-width="2.5"/></svg><strong>No Income Limits, No DTI<br>Restrictions, No Property<br>Restrictions</strong></li>
  </ul>

  <div class="brand-box"><i class="mark"></i><span>2nd Lane Home Lending</span></div>

  <div class="contact">
    <p class="phone">Call (800) 471-9026</p>
    <p class="more">for more information</p>
    <p class="web">WWW.2NDLANEHOMES.COM</p>
  </div>

  <div class="housing-badge" aria-hidden="true"></div>
  <div class="license">RLCB #738160</div>
</main>
</body>
</html>
```